Editorial / Brochure Designer – Adobe InDesign Luxury Travel Publication Redesign

CREATIVE BRIEF
Editorial / Brochure Designer – Adobe InDesign
Luxury Travel Publication Redesign

Project:
Company brochure redesign — Endless Voyages for Harbor Lantern. Premium, full-color print publication.

Current State:
106-page brochure built on a stock design template. While the content foundation is strong, the design and layout repeat the same formula across all seven major sections.

Target Length:
Approximately 75–85 pages after planned content edits and consolidation. We are open to the designer's recommendations once the revised copy is reviewed and flowed into the new design.

Format:
8.5" × 11" portrait finished pages with 11" × 17" facing-page spreads. Full-color professional print production. Final binding is TBD, likely perfect/PUR perfect binding.

Audience:
Existing referral clients, including clients we would like to re-engage, as well as new referrals. Our clients are loyal, often multigenerational, higher-end travelers planning meaningful vacations, celebrations, and bucket-list journeys.

Primary Goal:
Create an evergreen "keep and refer back to" publication—not a seasonal mailer. The brochure should avoid dates, "new in 2027" messaging, or other content that will quickly expire.

Brand Feel:
Personal, relationship-driven, sophisticated, inspiring and "different and outside the box." It should not feel like a generic luxury travel agency brochure or stock/template design.

Think premium travel magazine / coffee-table publication rather than a traditional travel catalog.

Must Avoid:
Template monotony. The existing brochure relies heavily on the same layout skeleton:

Section divider → headline → pitch → bullet list → repeat

The redesigned publication must introduce variety in pacing, layout, photography, typography, white space, and visual rhythm from section to section, while still feeling cohesive and unmistakably Harbor Lantern.

The Design Challenge
This is not simply a cleanup or reformatting project.

The selected designer will receive the existing 106-page brochure as the content foundation, along with revised/trimmed copy, brand assets, photography, and detailed editorial recommendations.

We want you to approach the publication with fresh eyes and a new creative perspective.

Some pages may need to become dramatic two-page spreads. Others may need to be minimal and quiet. Some information may work better as an editorial feature, comparison, sidebar, testimonial, pull quote, or visual story.

We want a designer who understands editorial pacing across a long publication, rather than simply creating an attractive template and repeating it.

Planned Content Changes/Priorities
The revised publication will include changes such as:

• Eliminating repetitive pages and messaging
• Creating one strong "Why Harbor Lantern" narrative
• Adding a personal "Meet Ruth" / founder story
• A personal "Meet Ruth" spread near the front — photo, founder story, why referrals are the only marketing you've ever needed
• A short "how we've grown" page/timeline showing the range of travel you now cover
• Introducing recurring "Ruth's Pick" editorial callouts
• Incorporating authentic client stories/testimonials per major section
• Removing or relocating time-sensitive content
• Section openers that feel distinct from each other in layout, not just in photo subject
• Strengthening the final call to action
• Bringing more personality and Harbor Lantern-specific storytelling into the publication

We specifically want someone with demonstrated experience designing:

• 50–150+ page publications
• Magazines
• Luxury brochures
• Product catalogs
• Lookbooks
• High-end print collateral
• Professional print publications

Experience with luxury travel, hospitality, lifestyle, cruise, resort, or premium consumer brands is highly desirable.

Advanced Adobe InDesign expertise is required, including Parent/Master Pages, paragraph and character styles, grids, long-document workflows, typography, image management, preflight, CMYK, bleeds, packaging, and professional print-ready PDF production.

We want to evaluate your:
• Creative direction
• Editorial judgment
• Typography
• Photography treatment
• Visual hierarchy
• Use of white space
• Page-to-page pacing
• Ability to elevate our existing brand

The successful designer will then be considered for the complete 75–85+ page publication redesign.

To Apply
Please provide:

• 2–4 examples of long-form publications you personally designed, preferably 50+ pages.
• Your experience with professional print production.
• Confirmation that you work in Adobe InDesign and can provide packaged source files so that we can edit at a later date.

Please prioritize relevant editorial work. We are specifically looking for long-form publication design experience, rather than portfolios focused primarily on logos, social media, websites, Canva templates, single-page flyers, or short brochures.

```html
<!DOCTYPE html>
<html lang="en">
<head>
<meta charset="utf-8">
<title>Harbor Lantern – Alaska &amp; The Caribbean Spread</title>
<link href="https://fonts.googleapis.com/css2?family=Philosopher:wght@400;700&family=Quicksand:wght@400;500;600&display=swap" rel="stylesheet">
<style>
  :root{
    --backdrop:#dcdcdd;
    --paper:#f6f6f6;
    --navy:#1f3a6e;
    --navy-box:#2c4a7c;
    --red:#a6252f;
    --ink:#4a4f5a;
    --frame:#e9e9ea;
    --white:#ffffff;
    --sep:#8a94ad;
  }
  *{box-sizing:border-box;margin:0;padding:0}
  html,body{width:1200px;height:900px;overflow:hidden;background:var(--backdrop)}
  body{font-family:"Quicksand",sans-serif;color:var(--ink);position:relative}
  .spread{position:absolute;left:20px;top:75px;width:1160px;height:750px;display:flex;box-shadow:0 6px 24px rgba(0,0,0,.18)}
  .page{position:relative;width:580px;height:750px;background:var(--paper);overflow:hidden}
  .page--left{border-right:1px solid #d2d2d2}
  .display{font-family:"Philosopher",sans-serif;font-weight:700;text-transform:uppercase}
  .photo{position:absolute}
  /* Left page */
  .alaska-hero{left:0;top:0;width:580px;height:330px;
    background:linear-gradient(180deg,#3a3f8a 0%,#8d5a8e 30%,#d97a5a 48%,#f0a640 56%,#7fa7c9 62%,#2f6f98 82%,#1c3f62 100%)}
  .alaska-title{position:absolute;left:26px;top:70px;font-size:76px;color:var(--white);letter-spacing:1px;text-shadow:0 2px 6px rgba(0,0,0,.45)}
  .headline{position:absolute;left:34px;top:348px;width:300px;font-size:22px;line-height:1.05;color:var(--navy)}
  .lede{position:absolute;left:34px;top:432px;width:296px;font-size:9.5px;line-height:1.45}
  .lede p{margin-bottom:4px}
  .sub{font-family:"Philosopher",sans-serif;font-weight:700;text-transform:uppercase;color:var(--navy);font-size:13.5px;margin-bottom:4px}
  .bullets{list-style:none;font-size:9.5px;line-height:1.5}
  .bullets li::before{content:"• "}
  .families-left{position:absolute;left:34px;top:530px;width:290px}
  .alaska-second{left:345px;top:355px;width:235px;height:305px;
    background:linear-gradient(160deg,#3f4f3a 0%,#6d7a3a 35%,#e8b25a 55%,#c9a46a 68%,#3f5a2c 100%)}
  .lines-left{position:absolute;left:30px;top:610px;width:300px;text-align:center}
  .lines-left .line{display:flex;gap:14px;margin-top:4px}
  .lines-left .line div{flex:1}
  .line-name{font-family:"Philosopher",sans-serif;font-weight:700;color:var(--navy);font-size:11px;text-transform:uppercase}
  .line-note{font-size:8.5px;line-height:1.35}
  .footer{position:absolute;left:26px;right:26px;bottom:20px;font-family:"Philosopher",sans-serif;font-weight:700;font-size:7px;color:var(--navy);letter-spacing:.1px;display:flex;justify-content:space-between;align-items:baseline;gap:8px;white-space:nowrap}
  .footer .sep{margin:0 4px;color:var(--sep)}
  .footer .folio{flex:none}
  /* Right page */
  .carib-title{position:absolute;right:30px;top:34px;font-size:60px;color:var(--red);line-height:1;text-align:right}
  .carib-sub{position:absolute;right:30px;top:98px;font-size:21px;color:var(--navy);line-height:1.1;text-align:right}
  .carib-frame{position:absolute;left:60px;top:160px;width:500px;height:250px;background:var(--frame)}
  .carib-photo{left:40px;top:175px;width:505px;height:215px;
    background:linear-gradient(180deg,#3e5a3a 0%,#6f7f6a 35%,#d99a5a 58%,#f2b56a 66%,#6f9fb2 80%,#3e6a80 100%)}
  .lines-box{position:absolute;left:30px;top:360px;width:240px;padding:14px 16px;background:var(--red);color:var(--white)}
  .lines-box .sub{color:var(--white)}
  .lines-box .line-name{color:var(--white);margin-top:6px}
  .lines-box .line-note{color:#f3dada}
  .carib-body{position:absolute;left:305px;top:420px;width:245px;font-size:9.5px;line-height:1.45}
  .carib-body p{margin-bottom:5px}
  .families-right{position:absolute;left:30px;top:520px;width:260px}
  .dest-box{position:absolute;left:330px;top:600px;width:220px;padding:14px 16px;background:var(--navy-box);color:var(--white)}
  .dest-box .sub{color:var(--white)}
  .dest-box .bullets{color:#dfe6f2}
</style>
</head>
<body>
<div class="spread">
  <section class="page page--left">
    <div class="photo alaska-hero" role="img" aria-label="Traveler in a red jacket overlooking a frozen waterfall under a vivid sunset sky"></div>
    <h1 class="display alaska-title">Alaska</h1>
    <h2 class="display headline">Where Wonder Is Shared and Remembered for a Lifetime</h2>
    <div class="lede">
      <p>An Alaska cruise offers a breathtaking backdrop for family connection. Towering glaciers, wildlife encounters, and awe-inspiring landscapes create unforgettable shared experiences.</p>
      <p>Watch whales surface together. Stand in silence as glaciers thunder into the sea. Explore charming frontier towns rich with history.</p>
    </div>
    <div class="families-left">
      <h3 class="sub">Why It Works for Families:</h3>
      <ul class="bullets">
        <li>Educational and inspiring for all ages.</li>
        <li>Comfortable, easy travel with minimal logistics.</li>
        <li>Shared “wow” moments every day.</li>
      </ul>
    </div>
    <div class="photo alaska-second" role="img" aria-label="Golden sunset over a green river valley with a hillside village"></div>
    <div class="lines-left">
      <h3 class="sub">Featured Cruise Lines:</h3>
      <div class="line">
        <div><div class="line-name">Meridian Line</div><div class="line-note">Ideal for active families with diverse onboard experiences.</div></div>
        <div><div class="line-name">Solstice Cruises</div><div class="line-note">Elevated comfort, refined dining, &amp; immersive excursions.</div></div>
      </div>
    </div>
    <footer class="footer">
      <span class="contact">HARBOR LANTERN<span class="sep">|</span>TOLL-FREE 1-800-555-0142<span class="sep">|</span>LOCAL 816-555-0178<span class="sep">|</span>RUTH@HARBORLANTERN.COM<span class="sep">|</span>WWW.HARBORLANTERN.COM</span>
      <span class="folio">P6</span>
    </footer>
  </section>

  <section class="page page--right">
    <h1 class="display carib-title">The Caribbean</h1>
    <h2 class="display carib-sub">Where Laughter Comes Easy<br>&amp; Time Slows Down</h2>
    <div class="carib-frame"></div>
    <div class="photo carib-photo" role="img" aria-label="Infinity pool deck overlooking a tropical bay at sunset"></div>
    <div class="lines-box">
      <h3 class="sub">Featured Cruise Lines:</h3>
      <div class="line-name">Meridian Line</div>
      <div class="line-note">Engaging, high-energy experiences perfect for families of all generations.</div>
      <div class="line-name">Solstice Cruises</div>
      <div class="line-note">Sophisticated atmosphere with modern luxury touches.</div>
    </div>
    <div class="carib-body">
      <p>The Caribbean offers the perfect blend of relaxation and adventure—ideal for bringing generations together in a seamless, stress-free setting, whether at sea or on land.</p>
      <p>From private island escapes and beachfront resorts to vibrant cultural excursions, each day is thoughtfully designed for both connection and personal freedom.</p>
      <p>Grandparents unwind. Kids explore. Families come together over sunset dinners, beachside laughter, and unforgettable shared moments.</p>
    </div>
    <div class="families-right">
      <h3 class="sub">Why It Works for Families:</h3>
      <ul class="bullets">
        <li>Warm weather and easy travel.</li>
        <li>Activities for every age and interest.</li>
        <li>Private destinations, all-inclusive resorts, and curated experiences.</li>
        <li>Flexible days that balance relaxation, exploration, and time together.</li>
      </ul>
    </div>
    <div class="dest-box">
      <h3 class="sub">Featured Destinations:</h3>
      <ul class="bullets">
        <li>Jamaica</li>
        <li>Mexico</li>
        <li>Dominican Republic</li>
      </ul>
    </div>
    <footer class="footer">
      <span class="contact">HARBOR LANTERN<span class="sep">|</span>TOLL-FREE 1-800-555-0142<span class="sep">|</span>LOCAL 816-555-0178<span class="sep">|</span>RUTH@HARBORLANTERN.COM<span class="sep">|</span>WWW.HARBORLANTERN.COM</span>
      <span class="folio">P7</span>
    </footer>
  </section>
</div>
</body>
</html>
```